Kinsmen Crest Beard Oil Label for 1oz dropper bottle

Create a label for a 1oz beard oil dropper bottle. The label is 1.5 inches tall and 2.75 inches wide. Our logo is listed in the brief so please use it but it doesnt have to be that prominent. BEARD OIL is the most important verbiage. We like elements of all the attached images but we want our own look and feel.

Target Market(s)

Men with beards

Requirements
Must have
• Kinsmen Crest Logo, BEARD OIL, Flavor (Tobacco Vanilla)

Ingredients
Fractionated Coconut Oil (MCT)
Golden Jojoba Oil
Hemp Seed Oil
Tea Tree Essential Oil
Orange Bitter Essential Oil
Peppermint Supreme Essential Oil
Tallow Aromas
DYE FREE

Directions:
Directions: apply 3-6 drops into your hand...rub oil into hands and apply directly onto beard. For best results massage into skin under beard area and work oil out towards beard. Discontinue use if skin becomes irritated.

100% MADE IN THE USA (American Flag 1 color)
Veteran Owned Co.
Nice to have
• Labels can change color with each flavor or a ring can change color to show flavor.

```html
<!DOCTYPE html>
<html lang="en">
<head>
<meta charset="utf-8">
<title>Kinsmen Crest Beard Oil Label</title>
<link rel="stylesheet" href="https://fonts.googleapis.com/css2?family=Jost:wght@500;600&family=Oswald:wght@500&family=Pathway+Gothic+One&display=swap">
<style>
  :root {
    --backdrop: #cfcfd2;
    --label-teal: #20363f;
    --label-dark: #121111;
    --ray: #3a3336;
    --cream: #e9e3cc;
    --orange: #f28c25;
    --orange-deep: #e26c17;
    --sticker: #ffffff;
  }
  * { margin: 0; padding: 0; box-sizing: border-box; }
  html, body { width: 1200px; height: 857px; overflow: hidden; background: var(--backdrop); }
  .canvas { position: relative; width: 1200px; height: 857px; }
  .label {
    position: absolute; left: 50px; top: 128px; width: 1100px; height: 600px; overflow: hidden;
    background: linear-gradient(180deg, var(--label-teal) 0%, #1c2d35 45%, var(--label-dark) 100%);
    color: var(--cream);
  }
  .rays {
    position: absolute; inset: 0;
    background: radial-gradient(ellipse at 50% 10%, rgba(70,58,62,0.55) 0%, rgba(58,51,54,0.25) 40%, rgba(0,0,0,0) 75%);
  }
  .panel { position: absolute; top: 0; height: 600px; width: 366px; }
  .panel--left { left: 0; }
  .panel--center { left: 367px; }
  .panel--right { left: 734px; }
  .panel-heading {
    font-family: "Oswald", sans-serif; font-weight: 500; font-size: 22px; letter-spacing: 0.12em;
    text-align: center; margin-top: 48px;
  }
  .panel-copy {
    font-family: "Pathway Gothic One", sans-serif; font-size: 26px; line-height: 36px;
    text-align: center; margin: 14px auto 0; width: 300px;
  }
  .usa-badge {
    position: absolute; left: 24px; top: 420px; width: 136px; height: 136px; border-radius: 50%;
    background: var(--cream);
  }
  .veteran-arc { position: absolute; left: 0; top: 20px; width: 366px; height: 120px; }
  .veteran-arc text {
    font-family: "Oswald", sans-serif; font-weight: 500; font-size: 30px; letter-spacing: 0.1em; fill: var(--cream);
  }
  .brand-name {
    position: absolute; left: 0; width: 366px; top: 140px; text-align: center;
    font-family: "Jost", sans-serif; font-weight: 600; font-size: 46px; line-height: 54px; color: var(--cream);
    text-transform: uppercase; letter-spacing: 0.02em;
  }
  .product-name {
    position: absolute; left: 0; width: 366px; top: 300px; text-align: center;
    font-family: "Jost", sans-serif; font-weight: 500; font-size: 92px; line-height: 88px; color: var(--orange);
  }
  .scent {
    position: absolute; left: 0; width: 366px; top: 506px; text-align: center;
    font-family: "Oswald", sans-serif; font-weight: 500; font-size: 24px; letter-spacing: 0.38em; padding-left: 0.38em;
  }
  .volume {
    position: absolute; left: 0; width: 366px; top: 546px; text-align: center;
    font-family: "Pathway Gothic One", sans-serif; font-size: 32px;
  }
  .ingredients { list-style: none; }
  .lot-sticker {
    position: absolute; left: 68px; top: 420px; width: 240px; height: 150px; background: var(--sticker);
  }
</style>
</head>
<body>
<main class="canvas">
  <section class="label" aria-label="Kinsmen Crest beard oil wrap label">
    <div class="rays" role="img" aria-label="Dark sunburst ray background"></div>

    <div class="panel panel--left">
      <h2 class="panel-heading">DIRECTIONS:</h2>
      <p class="panel-copy">Apply 3-6 drops into your hand. Rub oil into hands and apply directly onto beard. For best results massage into skin under beard area and work oil out towards beard. Discontinue use if skin becomes irritated.</p>
      <div class="usa-badge" role="img" aria-label="Made in USA one-colour flag badge"></div>
    </div>

    <div class="panel panel--center">
      <svg class="veteran-arc" viewBox="0 0 366 120" aria-label="Veteran Owned Co.">
        <defs><path id="veteran-curve" d="M 28 112 Q 183 10 338 112"/></defs>
        <text><textPath href="#veteran-curve" startOffset="50%" text-anchor="middle">•VETERAN OWNED CO.•</textPath></text>
      </svg>
      <div class="brand-name">Kinsmen<br>Crest</div>
      <h1 class="product-name">BEARD<br>OIL</h1>
      <div class="scent">TOBACCO VANILLA</div>
      <div class="volume">1oz</div>
    </div>

    <div class="panel panel--right">
      <h2 class="panel-heading">INGREDIENTS:</h2>
      <ul class="panel-copy ingredients">
        <li>Fractionated Coconut Oil (MCT)</li>
        <li>Golden Jojoba Oil</li>
        <li>Hemp Seed Oil</li>
        <li>Tea Tree Essential Oil</li>
        <li>Orange Bitter Essential Oil</li>
        <li>Peppermint Supreme Essential Oil</li>
        <li>Tallow Aromas</li>
        <li>DYE FREE</li>
      </ul>
      <div class="lot-sticker"></div>
    </div>
  </section>
</main>
</body>
</html>
```